Book cover entitled #GLOWBEYONDIT

Design front book cover (self-self-portait photos included) for my first book entitled -

#GLOWBEYONDIT (may be best to have different shades of colour for glow beyond it to stand off you). I'm intentionally choosing a title that is essentially a hashtag.

Subtitle - Rewriting quiet inner battles

Concept of cover - left side of my face is shaded with shame and right side is brighter and hopeful. I have also include my logo.

Link for photos
https://www.filqorvex.com/sh/tq7mxd2kw9pl41a/BBR8NpXwQ3hLm6TzvKe2YUJ5b?dl=0

Target Market(s)

People (or friends & family) suffering with the shame of mental health struggles

Industry/Entity Type

Mental Health

Font styles to use
Other font styles liked:
• Avenir

Colors
3276b5
85acd3
cfdeed

Requirements
Must have
• Relatable, contemporary, authentic & compelling
• Link for photos
• https://www.filqorvex.com/sh/tq7mxd2kw9pl41a/BBR8NpXwQ3hLm6TzvKe2YUJ5b?dl=0
Nice to have
• Abstract & creative
Should not have
• Cheesy, plastic, pedestrian etc

```html
<!DOCTYPE html>
<html lang="en">
<head>
<meta charset="UTF-8">
<title>#GLOWBEYONDIT — Book Cover</title>
<link rel="stylesheet" href="https://fonts.googleapis.com/css2?family=Oswald:wght@600&family=Nunito+Sans:wght@400&display=swap">
<style>
  :root {
    --ink: #000000;
    --shadow: #07090e;
    --skin-deep: #7a3f1a;
    --skin: #d08650;
    --skin-light: #f0b07c;
    --hair: #2a2a2a;
    --jacket: #1b2438;
    --silver-dark: #a8a8a8;
    --silver: #d6d6d6;
    --silver-light: #f4f4f4;
    --title-yellow: #ffd83a;
    --title-white: #ffffff;
    --title-blue: #18a9e8;
    --subtitle: #f5d93a;
    --author: #ffffff;
  }
  * { margin: 0; padding: 0; box-sizing: border-box; }
  html, body {
    width: 776px;
    height: 1200px;
    overflow: hidden;
    background: var(--ink);
  }
  .cover {
    position: relative;
    width: 776px;
    height: 1200px;
    overflow: hidden;
    background: var(--ink);
  }
  .portrait {
    position: absolute;
    inset: 0;
    background:
      linear-gradient(90deg, var(--ink) 0%, var(--ink) 34%, rgba(0,0,0,0.75) 44%, transparent 58%),
      linear-gradient(180deg, transparent 0%, transparent 66%, var(--jacket) 80%, var(--shadow) 100%),
      radial-gradient(ellipse 27% 30% at 62% 44%, var(--skin-light) 0%, var(--skin) 45%, var(--skin-deep) 78%, transparent 100%),
      radial-gradient(ellipse 34% 20% at 58% 14%, var(--hair) 0%, var(--hair) 55%, transparent 100%),
      linear-gradient(150deg, var(--silver-light) 0%, var(--silver) 50%, var(--silver-dark) 100%);
  }
  .title {
    position: absolute;
    left: 88px;
    top: 52px;
    width: 112px;
    height: 950px;
  }
  .title text {
    font-family: "Oswald", "Arial Narrow", sans-serif;
    font-weight: 600;
    font-size: 146px;
  }
  .brand {
    position: absolute;
    left: 48px;
    top: 1042px;
    width: 150px;
    display: flex;
    flex-direction: column;
    align-items: center;
    gap: 8px;
  }
  .brand-mark {
    width: 84px;
    height: 84px;
    border-radius: 50%;
    background: var(--author);
  }
  .brand-name {
    font-family: "Nunito Sans", "Avenir", sans-serif;
    font-weight: 400;
    font-size: 30px;
    line-height: 1;
    letter-spacing: 0.5px;
    color: var(--author);
    white-space: nowrap;
  }
  .subtitle {
    position: absolute;
    left: 258px;
    top: 1124px;
    width: 472px;
    font-family: "Oswald", "Arial Narrow", sans-serif;
    font-weight: 600;
    font-size: 30px;
    line-height: 1;
    letter-spacing: 1.2px;
    color: var(--subtitle);
    text-transform: uppercase;
    text-align: right;
    white-space: nowrap;
  }
</style>
</head>
<body>
  <main class="cover">
    <div class="portrait" role="img" aria-label="Portrait photograph of the author, left half of the face in deep shadow and right half warmly lit against a brushed silver backdrop, wearing a dark navy jacket"></div>

    <svg class="title" viewBox="0 0 112 950" aria-label="#GLOWBEYONDIT">
      <defs>
        <linearGradient id="title-glow" x1="0" y1="0" x2="1" y2="0">
          <stop offset="0" stop-color="var(--title-yellow)"/>
          <stop offset="0.36" stop-color="var(--title-yellow)"/>
          <stop offset="0.5" stop-color="var(--title-white)"/>
          <stop offset="0.7" stop-color="var(--title-white)"/>
          <stop offset="0.84" stop-color="var(--title-blue)"/>
          <stop offset="1" stop-color="var(--title-blue)"/>
        </linearGradient>
      </defs>
      <text transform="translate(106 950) rotate(-90)" x="0" y="0"
            textLength="950" lengthAdjust="spacingAndGlyphs"
            fill="url(#title-glow)">#GLOWBEYONDIT</text>
    </svg>

    <div class="brand">
      <span class="brand-mark" aria-hidden="true"></span>
      <p class="brand-name">dane carlow</p>
    </div>
    <p class="subtitle">Rewriting quiet inner battles</p>
  </main>
</body>
</html>
```